Copper Ridge Business Cards For New Startup

I am looking for you to design some business cards for a new startup https://copperridgehub.example. I have supplied logo, brand guidelines and our signatures as a guide.

We need this to reflect the brand guidelines and the website for brand consistency,

What is Copper Ridge?

Mallorca's Business Growth Community
Join your new business community full of passionate entrepreneurs who
love to solve problems and help each other grow together!

Any questions you can ask.

Target Market(s)

Business to Business

Contact Information for Business Card

These are attached (signatures) to the job

Font styles to use
Other font styles liked:
• Open Sans

Requirements
Must have
• Match design guidelines
Nice to have
• Photos of our faces so people remember us

```html
<!DOCTYPE html>
<html lang="en">
<head>
<meta charset="utf-8">
<title>Copper Ridge – Business Cards</title>
<link rel="stylesheet" href="https://fonts.googleapis.com/css2?family=Open+Sans:wght@400;600;700&display=swap">
<style>
  :root {
    --brand-olive: #676b2e;
    --paper: #ffffff;
    --ink: #111111;
  }
  html, body {
    margin: 0;
    padding: 0;
    width: 1200px;
    height: 1200px;
    overflow: hidden;
    background: var(--paper);
    font-family: "Open Sans", Arial, sans-serif;
  }
  .canvas {
    position: relative;
    width: 1200px;
    height: 1200px;
  }
  .card {
    position: absolute;
    left: 290px;
    width: 620px;
    height: 379px;
    box-sizing: border-box;
  }
  .card--front {
    top: 190px;
    background: var(--brand-olive);
  }
  .card--back {
    top: 631px;
    background: var(--paper);
    border: 2px solid var(--brand-olive);
    overflow: hidden;
  }
  .brand-lockup {
    position: absolute;
    left: 110px;
    top: 150px;
    display: flex;
    align-items: center;
    gap: 26px;
    color: var(--paper);
  }
  .brand-lockup__mark {
    width: 84px;
    height: 80px;
    display: block;
  }
  .brand-lockup__name {
    font-size: 46px;
    font-weight: 600;
    letter-spacing: 0.5px;
    line-height: 1;
    white-space: nowrap;
  }
  .back-mark {
    position: absolute;
    right: 34px;
    top: 32px;
    width: 70px;
    height: 66px;
  }
  .holder {
    position: absolute;
    left: 34px;
    top: 114px;
  }
  .holder__name {
    margin: 0;
    color: var(--brand-olive);
    font-size: 22px;
    font-weight: 700;
    letter-spacing: 1.2px;
  }
  .holder__role {
    margin: 22px 0 0;
    color: var(--ink);
    font-size: 16px;
    line-height: 24px;
    letter-spacing: 0.8px;
  }
  .social-row {
    position: absolute;
    left: 34px;
    top: 280px;
    display: flex;
    gap: 8px;
    margin: 0;
    padding: 0;
    list-style: none;
  }
  .social-row__item {
    width: 21px;
    height: 21px;
    background: var(--brand-olive);
  }
  .contact-line {
    position: absolute;
    left: 34px;
    right: 34px;
    top: 321px;
    margin: 0;
    color: var(--ink);
    font-size: 13px;
    letter-spacing: 0.4px;
    white-space: nowrap;
  }
</style>
</head>
<body>
<main class="canvas">
  <section class="card card--front" aria-label="Card front">
    <div class="brand-lockup">
      <svg class="brand-lockup__mark" viewBox="0 0 84 80" aria-hidden="true">
        <circle cx="42" cy="40" r="38" fill="none" stroke="currentColor" stroke-width="2"/>
      </svg>
      <span class="brand-lockup__name">COPPER RIDGE</span>
    </div>
  </section>

  <section class="card card--back" aria-label="Card back">
    <svg class="back-mark" viewBox="0 0 70 66" aria-hidden="true">
      <circle cx="35" cy="33" r="31" fill="none" stroke="var(--brand-olive)" stroke-width="2.5"/>
    </svg>
    <div class="holder">
      <h1 class="holder__name">Martin Hale</h1>
      <p class="holder__role">Founder &amp; Growth Hacker<br>Copper Ridge</p>
    </div>
    <ul class="social-row" aria-label="Social channels">
      <li class="social-row__item"></li>
      <li class="social-row__item"></li>
      <li class="social-row__item"></li>
      <li class="social-row__item"></li>
      <li class="social-row__item"></li>
    </ul>
    <p class="contact-line">M: +34 600 412 390 | E: mh@copperridgehub.example | copperridgehub.example</p>
  </section>
</main>
</body>
</html>
```